Dentistry

Dentist's personal business card. No logo needed. The card shoul deliver the massage of reliability, professionalism, experience.
Please ad the full brief of the project: down the line it says: the winning look should be precise and pristine NO pictures of Teeth, smiles, instruments etc.

The details to be desplaid are:
Dr. Lev Oranbury
Doctor of Dental Surgery
PHD
Web. Www.droranbury.example
Email. Lev@droranbury.example
Tel 07700900318
Surgery address. 27Bfernwick road London SE4 7QX UK
62 Harlow Crescent London EC3V 9PD. Uk

Industry/Entity Type

Massage

Requirements
Should not have
• Logo, teeth, smile any sort of instruments.

```html
<!DOCTYPE html>
<html lang="en">
<head>
<meta charset="utf-8">
<title>Dr. Lev Oranbury — Business Card</title>
<link rel="stylesheet" href="https://fonts.googleapis.com/css2?family=Tinos:wght@400;700&display=swap">
<style>
  :root {
    --page-bg: #ecebe8;
    --front-light: #e6e6e6;
    --front-mid: #d2d2d2;
    --front-edge: #bdbdbd;
    --name-dark: #2b2b2b;
    --accent-blue: #3a8cff;
    --rule-blue: #9cc6f2;
    --band-light: #2a74e8;
    --band-dark: #0b2494;
    --band-text: #5ea8ff;
    --ink: #111111;
    --paper: #ffffff;
  }
  * { margin: 0; padding: 0; box-sizing: border-box; }
  html, body {
    width: 947px;
    height: 1200px;
    overflow: hidden;
  }
  body {
    background: var(--page-bg);
    font-family: "Tinos", "Times New Roman", serif;
    position: relative;
  }
  .card {
    position: absolute;
    left: 84px;
    width: 758px;
    box-shadow: 2px 4px 10px rgba(0,0,0,0.35);
  }

  /* Front side */
  .card-front {
    top: 136px;
    height: 406px;
    background: linear-gradient(to bottom, var(--front-edge) 0%, var(--front-mid) 22%, var(--front-light) 50%, var(--front-mid) 78%, var(--front-edge) 100%);
    border: 1px solid #a9a9a9;
    text-align: center;
  }
  .front-name {
    position: absolute;
    left: 0; right: 0;
    top: 162px;
    font-size: 56px;
    font-weight: 400;
    color: var(--name-dark);
    text-shadow: 1px 2px 2px rgba(0,0,0,0.35);
    line-height: 1;
  }
  .front-title {
    position: absolute;
    left: 0; right: 0;
    top: 227px;
    font-size: 31px;
    color: var(--accent-blue);
    line-height: 1;
  }

  /* Back side */
  .card-back {
    top: 659px;
    height: 403px;
    background: var(--paper);
    overflow: hidden;
  }
  .back-name {
    position: absolute;
    left: 80px;
    top: 64px;
    font-size: 44px;
    font-weight: 400;
    color: var(--accent-blue);
    text-shadow: 1px 1px 1px rgba(0,0,0,0.25);
    line-height: 1;
    white-space: nowrap;
  }
  .back-credential {
    position: absolute;
    left: 80px;
    font-size: 20px;
    color: var(--ink);
    line-height: 24px;
  }
  .back-credential.degree { top: 107px; }
  .back-credential.phd { top: 138px; }
  .back-rule {
    position: absolute;
    left: 80px;
    top: 168px;
    width: 630px;
    height: 1px;
    background: var(--rule-blue);
  }
  .contact-line {
    position: absolute;
    right: 50px;
    text-align: right;
    font-size: 19px;
    color: var(--ink);
    line-height: 25px;
    white-space: nowrap;
  }
  .contact-line.tel { top: 186px; }
  .contact-line.address-main { top: 218px; }
  .contact-line.address-second { top: 284px; }
  .footer-band {
    position: absolute;
    left: 0; right: 0;
    bottom: 0;
    height: 66px;
    background: linear-gradient(to bottom, var(--band-light) 0, var(--band-light) 5px, var(--band-dark) 5px, var(--band-dark) 100%);
    display: flex;
    justify-content: space-between;
    align-items: center;
    padding: 5px 50px 0 55px;
    font-size: 19px;
    color: var(--band-text);
  }
</style>
</head>
<body>
  <section class="card card-front" aria-label="Card front">
    <h1 class="front-name">Dr. Lev Oranbury</h1>
    <p class="front-title">Doctor of Dental Surgery</p>
  </section>

  <section class="card card-back" aria-label="Card back">
    <h2 class="back-name">Dr. Lev Oranbury</h2>
    <p class="back-credential degree">Doctor of Dental Surgery</p>
    <p class="back-credential phd">PHD</p>
    <div class="back-rule"></div>
    <p class="contact-line tel">tel: 07700900318</p>
    <p class="contact-line address-main">27Bfernwick road,<br>London SE4 7QX UK;</p>
    <p class="contact-line address-second">62 Harlow Crescent<br>London EC3V 9PD. Uk</p>
    <footer class="footer-band">
      <span class="web">web: www.droranbury.example</span>
      <span class="email">e-mail: lev@droranbury.example</span>
    </footer>
  </section>
</body>
</html>
```